Business Card Design for Engineering Firm

Need a business card design for small mechanical and plumbing engineering form based in Utah. Design should be customizable for all employees.

```html
<!DOCTYPE html>
<html lang="en">
<head>
<meta charset="utf-8">
<title>Ridgeline Engineering – Business Card</title>
<link href="https://fonts.googleapis.com/css2?family=Lato:wght@400;700;900&display=swap" rel="stylesheet">
<style>
  :root {
    --brand-red: #7d0000;
    --ink-gray: #4a4a4a;
    --text-gray: #555555;
    --card-white: #ffffff;
    --backdrop: #3a3c3f;
  }
  html, body {
    margin: 0;
    padding: 0;
    width: 1200px;
    height: 952px;
    overflow: hidden;
    background: var(--backdrop);
    font-family: "Lato", sans-serif;
  }
  .stage {
    position: relative;
    width: 1200px;
    height: 952px;
  }
  .card {
    position: absolute;
    top: 321px;
    width: 540px;
    height: 310px;
    border-radius: 22px;
    overflow: hidden;
    box-shadow: 0 10px 30px rgba(0,0,0,0.35);
  }
  /* Front */
  .card-front {
    left: 40px;
    background: var(--card-white);
  }
  .person {
    position: absolute;
    left: 34px;
    top: 30px;
  }
  .person-name {
    margin: 0;
    font-size: 22px;
    font-weight: 400;
    color: var(--brand-red);
    letter-spacing: 0.5px;
  }
  .person-name strong { font-weight: 900; }
  .person-role {
    margin: 2px 0 0;
    font-size: 11px;
    color: var(--text-gray);
  }
  .brand-block {
    position: absolute;
    left: 34px;
    top: 128px;
    width: 120px;
    height: 120px;
    background: var(--brand-red);
  }
  .contact-list {
    position: absolute;
    right: 30px;
    top: 110px;
    margin: 0;
    padding: 0;
    list-style: none;
    text-align: right;
  }
  .contact-item {
    display: flex;
    justify-content: flex-end;
    align-items: center;
    gap: 10px;
    font-size: 12.5px;
    color: var(--text-gray);
    line-height: 1.3;
    margin-bottom: 6px;
  }
  .contact-item.address { margin-bottom: 12px; }
  .icon {
    width: 18px;
    height: 18px;
    border-radius: 3px;
    background: var(--brand-red);
    flex: none;
  }
  .icon.dark { background: var(--ink-gray); }
  .wordmark-front {
    position: absolute;
    left: 190px;
    bottom: 30px;
    color: var(--brand-red);
    font-weight: 700;
  }
  .wordmark-name {
    display: block;
    font-size: 30px;
    letter-spacing: 1px;
    line-height: 1;
  }
  .wordmark-tag {
    display: block;
    font-size: 12px;
    letter-spacing: 7px;
    margin-top: 4px;
  }
  /* Back */
  .card-back {
    left: 620px;
    background: var(--brand-red);
    display: flex;
    align-items: center;
    justify-content: center;
    gap: 22px;
  }
  .back-square {
    width: 44px;
    height: 44px;
    background: var(--card-white);
  }
  .back-divider {
    width: 1px;
    height: 70px;
    background: var(--card-white);
  }
  .wordmark-back {
    color: var(--card-white);
    font-weight: 700;
  }
</style>
</head>
<body>
<main class="stage">
  <section class="card card-front">
    <div class="person">
      <h1 class="person-name">DANIEL M. <strong>HARLOW</strong></h1>
      <p class="person-role">Managing Director</p>
    </div>
    <div class="brand-block"></div>
    <ul class="contact-list">
      <li class="contact-item address">
        <span>2140 Canyon Ridge Drive<br>Provo, UT 84604</span>
        <svg class="icon dark" viewBox="0 0 18 18"><rect width="18" height="18" rx="3" fill="#4a4a4a"/><path d="M9 3.5a3.6 3.6 0 0 0-3.6 3.6C5.4 10 9 14.5 9 14.5s3.6-4.5 3.6-7.4A3.6 3.6 0 0 0 9 3.5z" fill="#fff"/><circle cx="9" cy="7.1" r="1.4" fill="#4a4a4a"/></svg>
      </li>
      <li class="contact-item">
        <span>+00 987 654 32</span>
        <svg class="icon" viewBox="0 0 18 18"><rect width="18" height="18" rx="3" fill="#7d0000"/><path d="M6 4l2 2.5-1.2 1.2a7 7 0 0 0 3.5 3.5L11.5 10 14 12l-1 2c-4.5 0-9-4.5-9-9z" fill="#fff"/></svg>
      </li>
      <li class="contact-item">
        <span>office@ridgelineeng.com</span>
        <svg class="icon" viewBox="0 0 18 18"><rect width="18" height="18" rx="3" fill="#7d0000"/><rect x="4" y="5.5" width="10" height="7" fill="none" stroke="#fff" stroke-width="1.3"/><path d="M4 5.5l5 4 5-4" fill="none" stroke="#fff" stroke-width="1.3"/></svg>
      </li>
      <li class="contact-item">
        <span>www.ridgelineeng.com</span>
        <svg class="icon" viewBox="0 0 18 18"><rect width="18" height="18" rx="3" fill="#7d0000"/><path d="M6 4l7 5-3 .8 2 3.6-1.4.8-2-3.6L6 12.5z" fill="#fff"/></svg>
      </li>
    </ul>
    <div class="wordmark-front">
      <span class="wordmark-name">RIDGELINE</span>
      <span class="wordmark-tag">ENGINEERING</span>
    </div>
  </section>

  <section class="card card-back">
    <div class="back-square"></div>
    <div class="back-divider"></div>
    <div class="wordmark-back">
      <span class="wordmark-name">RIDGELINE</span>
      <span class="wordmark-tag">ENGINEERING</span>
    </div>
  </section>
</main>
</body>
</html>
```